We are committed to helping players reach Football greatness!

Target Market(s)

Sports enthusiasts between 9 to 18 and their parents of all backgrounds.

Contact Information for Business Card

Harbor Football Academy
Marcus Delacourt
Head Coach
0452 318 627
harborfta@mailnest.test

Logo Text

Harbor Football Academy

Logo styles of interest
Abstract Logo
Requirements
Must have
• I want the logo to be representing football (soccer) and try and make it as 3D as possible please.
Nice to have
• As above mentioned make it represent a Football (soccer) theme please.
Should not have
• Nothing non-child friendly please.

```html
<!DOCTYPE html>
<html lang="en">
<head>
<meta charset="utf-8">
<title>Harbor Football Academy – Business Card</title>
<link rel="stylesheet" href="https://fonts.googleapis.com/css2?family=Marcellus+SC&family=Quicksand:wght@400&display=swap">
<style>
  :root {
    --ink-blue: #0a3de6;
    --paper: #ffffff;
    --band-light: #5ee6fa;
    --band-deep: #2ed5f1;
    --mark-light: #4ff0ff;
    --mark-deep: #0a40f0;
  }
  html, body {
    margin: 0;
    padding: 0;
    overflow: hidden;
    background: var(--paper);
  }
  .card {
    position: relative;
    width: 1200px;
    height: 695px;
    background: var(--paper);
    overflow: hidden;
    color: var(--ink-blue);
  }
  .card-art {
    position: absolute;
    inset: 0;
  }
  .tagline, .academy-name, .phone, .email {
    font-family: "Marcellus SC", serif;
    font-variant: small-caps;
  }
  .tagline {
    position: absolute;
    top: 26px;
    left: 0;
    width: 1200px;
    text-align: center;
    font-size: 21px;
    letter-spacing: 0.5px;
    text-transform: lowercase;
  }
  .tagline::first-letter { text-transform: uppercase; }
  .academy-name {
    position: absolute;
    top: 222px;
    left: 0;
    width: 1336px;
    text-align: center;
    font-size: 54px;
    letter-spacing: 1px;
    margin: 0;
    font-weight: 400;
  }
  .person {
    position: absolute;
    top: 416px;
    left: 453px;
    width: 328px;
    text-align: center;
    font-family: "Quicksand", sans-serif;
  }
  .person-name {
    font-size: 36px;
    line-height: 48px;
    padding-bottom: 8px;
    border-bottom: 1px solid var(--ink-blue);
  }
  .person-role {
    font-size: 30px;
    line-height: 44px;
    margin-top: 4px;
  }
  .phone {
    position: absolute;
    top: 622px;
    left: 0;
    width: 1245px;
    text-align: center;
    font-size: 27px;
  }
  .email {
    position: absolute;
    top: 651px;
    left: 0;
    width: 1250px;
    text-align: center;
    font-size: 24px;
    text-transform: lowercase;
  }
</style>
</head>
<body>
  <div class="card">
    <svg class="card-art" width="1200" height="695" viewBox="0 0 1200 695" aria-hidden="true">
      <defs>
        <linearGradient id="mark-fill" x1="0" y1="0" x2="0" y2="1">
          <stop offset="0" stop-color="var(--mark-light)"/>
          <stop offset="1" stop-color="var(--mark-deep)"/>
        </linearGradient>
      </defs>
      <g class="rule-lines" stroke="var(--ink-blue)" stroke-width="1.2">
        <line x1="0" y1="40" x2="74" y2="40"/>
        <line x1="1138" y1="40" x2="1200" y2="40"/>
        <line x1="362" y1="637" x2="466" y2="637"/>
        <line x1="779" y1="637" x2="883" y2="637"/>
      </g>
      <g class="banner-band">
        <rect x="6" y="301" width="1189" height="53" fill="var(--band-light)"/>
        <rect x="6" y="354" width="1189" height="44" fill="var(--band-deep)"/>
      </g>
      <circle class="brand-dot" cx="142" cy="354" r="100" fill="url(#mark-fill)"/>
    </svg>

    <div class="tagline">Sports enthusiasts between 9 to 18 and their parents of all backgrounds</div>
    <h1 class="academy-name">Harbor Football Academy</h1>

    <div class="person">
      <div class="person-name">Marcus Delacourt</div>
      <div class="person-role">Head Coach</div>
    </div>

    <div class="phone">Ph.:0452 318 627</div>
    <div class="email">harborfta@mailnest.test</div>
  </div>
</body>
</html>
```